Lumora vale- referral cards for new customers

Hey,

I would like 1 set of business cards with the following details:

10% off any sales / coupon code
Our phone number: 4702938165
Menu :Lumoravale.example (for the menu)
A line left blank to hand write an activation code: either on top or just on one side

Include the Lumora Vale logo ( your choice of black or white logo)
This card is to drive orders for people to order a cannabis order with Lumora Vale. Please make the logo a large part of the card on both sides.

Target Market(s)

People who consume cannabis 21 and up

Industry/Entity Type

Business

Contact Information for Business Card

This business card will be given to customers so they can then give it to other customers and generate referalls. We need this card to be elegant, impressionable, professional, and something worth keeping and passing to friends.

Font styles to use
Decorative
Script

Colors
33a6d7
85acd3
3176b5
0455a3
0592cd
85cae6
cee9f5
eaf1f7
757575

Requirements
Must have
• Our website
• Phone Number
• The 10% off an order
• Spot for activation code
Nice to have
• Eye catching design
• Look classy
• Textured feel or textured look
Should not have
• Do not look super cannabis heady
• Do not look attractive to children

```html
<!DOCTYPE html>
<html lang="en">
<head>
<meta charset="utf-8">
<title>Lumora Vale – Referral Cards</title>
<link href="https://fonts.googleapis.com/css2?family=Lato:wght@400;700&display=swap" rel="stylesheet">
<style>
  :root {
    --page: #ecece8;
    --card-sky: #c3e6ea;
    --olive: #585d28;
    --ink: #262626;
    --paper: #ffffff;
  }
  * { margin: 0; padding: 0; box-sizing: border-box; }
  html, body {
    width: 1200px;
    height: 900px;
    overflow: hidden;
    background: var(--page);
    font-family: "Lato", sans-serif;
  }
  .canvas {
    position: relative;
    width: 1200px;
    height: 900px;
  }
  .card {
    position: absolute;
    left: 320px;
    width: 560px;
    height: 320px;
    background: var(--card-sky);
    overflow: hidden;
    box-shadow: 0 6px 18px rgba(0,0,0,0.18);
  }
  .card--back { top: 100px; }
  .card--front { top: 480px; }
  .card svg { position: absolute; inset: 0; }

  .brand-name {
    position: absolute;
    font-family: "Lato", sans-serif;
    font-weight: 700;
    color: var(--ink);
    letter-spacing: 0.04em;
    line-height: 1;
  }
  .card--back .brand-name {
    left: 0; right: 0; top: 170px;
    text-align: center;
    font-size: 26px;
  }
  .card--front .brand-name {
    left: 60px; top: 184px;
    font-size: 30px;
  }

  .web-band {
    position: absolute;
    left: 0; right: 0; bottom: 0;
    height: 86px;
    background: var(--olive);
    color: var(--paper);
    display: flex;
    align-items: center;
    justify-content: center;
    font-size: 17px;
    letter-spacing: 0.16em;
  }

  .activation {
    position: absolute;
    top: 30px;
    right: 28px;
    font-size: 13px;
    line-height: 1;
    color: var(--ink);
    letter-spacing: 0.03em;
    display: flex;
    align-items: flex-end;
    gap: 8px;
  }
  .activation__line {
    width: 110px;
    border-bottom: 1px dashed var(--ink);
    height: 12px;
  }

  .call {
    position: absolute;
    left: 36px;
    bottom: 18px;
    color: var(--paper);
    font-size: 22px;
    line-height: 1;
  }
</style>
</head>
<body>
<main class="canvas">

  <section class="card card--back" aria-label="Card back">
    <svg width="560" height="320" viewBox="0 0 560 320" aria-hidden="true">
      <circle class="brand-mark" cx="280" cy="95" r="62" fill="#585d28"/>
    </svg>
    <p class="brand-name">Lumora Vale</p>
    <p class="web-band">WWW.LUMORAVALE.EXAMPLE</p>
  </section>

  <section class="card card--front" aria-label="Card front">
    <svg width="560" height="320" viewBox="0 0 560 320">
      <circle class="brand-mark" cx="170" cy="98" r="62" fill="#585d28"/>
      <polygon class="call-band" points="0,262 560,200 560,320 0,320" fill="#585d28"/>
      <polygon class="offer-burst" fill="#585d28" transform="translate(0 25)"
        points="465,40 481,90 520,55 509,106 560,95 525,134 575,150 525,166 560,205 509,194 520,245 481,210 465,260 449,210 410,245 421,194 370,205 405,166 355,150 405,134 370,95 421,106 410,55 449,90"/>
      <g transform="translate(478 183) rotate(-62)" fill="#ffffff" font-family="Lato, sans-serif" text-anchor="middle">
        <text class="offer-main" y="-4" font-size="26" font-weight="700">10% OFF</text>
        <text class="offer-sub" y="18" font-size="15">AN ORDER</text>
      </g>
    </svg>
    <p class="activation">ACTIVATION CODE <span class="activation__line"></span></p>
    <p class="brand-name">Lumora Vale</p>
    <p class="call">Call: 4702938165</p>
  </section>

</main>
</body>
</html>
```